Autodetailing namecard design: Rose Gold Lettering on Black Matt

This is a namecard design project
requiring two-sided design
Base Color of Namecard: black matt

On front:
Company name,
"Lumina Finishes 14 Cendana"
Subtext: Auto Detailing Studio

Name of card holder: Marcus Oyelaran
Phone Number: +6011-4837-5062
address: 14, Jalan Cendana 5/3Taman Seri Cendana, 81400 Johor Bahru, Johor, Malaysia

Back:
Our Services
High Gloss Car Paint Protection
Custom Color Modification and Styling
Anti-Chip Glass Protection Film
Heat Rejection Glass Tinting

Target Market(s)

Autodetailing for highend cars

Contact Information for Business Card

as mentioned in project details

Colors

Designer to choose colors to be used in the design.

Requirements
Must have
• The main value-add to this project is the design of a logo suited for our purpose and name, and the inclusion of business card details into the card design

```html
<!DOCTYPE html>
<html lang="en">
<head>
<meta charset="utf-8">
<title>Lumina Finishes 14 Cendana – Business Card</title>
<link rel="stylesheet" href="https://fonts.googleapis.com/css2?family=Lato:wght@400;700&display=swap">
<style>
  :root {
    --backdrop: #2b2b2d;
    --card-matt: #151516;
    --rose: #d39681;
    --rose-light: #e8bcaa;
    --rose-deep: #b4705d;
    --back-top: #eab7a7;
    --back-bottom: #dc9f8c;
    --ink: #111111;
    --light-text: #e9e4e2;
  }
  * { margin: 0; padding: 0; box-sizing: border-box; }
  html, body { width: 1200px; height: 1200px; overflow: hidden; }
  body {
    background: var(--backdrop);
    font-family: "Lato", sans-serif;
    position: relative;
  }
  .card {
    position: absolute;
    top: 310px;
    height: 594px;
    box-shadow: 0 2px 8px rgba(0,0,0,.6);
  }
  .card-front {
    left: 234px;
    width: 364px;
    background: var(--card-matt);
    text-align: center;
  }
  .brand {
    position: absolute;
    top: 100px;
    left: 0; right: 0;
    display: flex;
    flex-direction: column;
    align-items: center;
  }
  .brand-row {
    display: flex;
    align-items: center;
    gap: 16px;
    height: 130px;
  }
  .brand-mark {
    width: 40px; height: 40px;
    border-radius: 50%;
    background: var(--rose);
    flex: none;
  }
  .brand-name {
    font-weight: 700;
    font-size: 30px;
    line-height: 1.15;
    color: var(--rose);
    text-align: left;
    letter-spacing: .5px;
  }
  .brand-sub {
    margin-top: 10px;
    font-size: 20px;
    color: var(--rose);
    letter-spacing: .2px;
    padding-bottom: 4px;
    border-bottom: 3px solid var(--rose);
    width: 264px;
  }
  .holder {
    position: absolute;
    top: 358px;
    left: 0; right: 0;
    font-size: 27px;
    font-weight: 700;
    color: var(--rose);
    letter-spacing: .3px;
  }
  .rule {
    position: absolute;
    left: 73px;
    width: 222px;
    height: 4px;
    background: linear-gradient(90deg, var(--rose-deep), var(--rose-light), var(--rose));
  }
  .rule-top { top: 406px; }
  .rule-bottom { top: 461px; }
  .phone {
    position: absolute;
    top: 424px;
    left: 0; right: 0;
    font-size: 21px;
    color: var(--light-text);
  }
  .address {
    position: absolute;
    top: 485px;
    left: 0; right: 0;
    font-size: 16.5px;
    line-height: 22px;
    color: var(--light-text);
    font-style: normal;
  }
  .card-back {
    left: 627px;
    width: 369px;
    background: linear-gradient(160deg, var(--back-top), var(--back-bottom));
    overflow: hidden;
  }
  .back-decor {
    position: absolute;
    inset: 0;
    background: radial-gradient(ellipse 80% 60% at 60% 45%, rgba(255,255,255,.12), rgba(255,255,255,0) 70%);
  }
  .services {
    position: absolute;
    top: 182px;
    left: 0; right: 0;
    text-align: center;
    color: var(--ink);
  }
  .services h2 {
    font-weight: 400;
    font-size: 27px;
    margin-bottom: 28px;
    letter-spacing: .2px;
  }
  .services ul { list-style: none; }
  .services li {
    font-size: 17.5px;
    line-height: 21px;
    margin-bottom: 14px;
  }
</style>
</head>
<body>
  <section class="card card-front">
    <div class="brand">
      <div class="brand-row">
        <span class="brand-mark"></span>
        <div class="brand-name">LUMINA FINISHES<br>14 CENDANA</div>
      </div>
      <div class="brand-sub">AUTO DETAILING STUDIO</div>
    </div>
    <div class="holder">MARCUS OYELARAN</div>
    <div class="rule rule-top"></div>
    <div class="phone">+6011-4837-5062</div>
    <div class="rule rule-bottom"></div>
    <address class="address">
      14, Jalan Cendana<br>
      5/3Taman Seri Cendana,<br>
      81400 Johor Bahru Johor, Malaysia
    </address>
  </section>

  <section class="card card-back">
    <div class="back-decor" role="img" aria-label="Faint enlarged brand emblem watermark"></div>
    <div class="services">
      <h2>OUR SERVICES</h2>
      <ul>
        <li>HIGH GLOSS CAR<br>PAINT PROTECTION</li>
        <li>CUSTOM COLOR MODIFICATION<br>AND STYLING</li>
        <li>ANTI-CHIP GLASS PROTECTION FILM</li>
        <li>HEAT REJECTION GLASS TINTING</li>
      </ul>
    </div>
  </section>
</body>
</html>
```